Group company Christmas wine label with Logo

We have 3 businesses with 3 distinct logos. Want a Christmas label for out wine bottlesd that we can use that includes all 3 companies or logo somehow.
We have an old logo that we put on last years label but need something new we are sick of it.
I will upload the old christmas logo as well as the 3 company logos. The companies are Fenwick & Dorr, Brightwave and KRTL
We want a slick professional label

Target Market(s)

professionals

Logo Text

2024 Merry Christmas from the team at Fenwick & Dorr, KRTL & Brightwave

Logo styles of interest
Pictorial/Combination Logo
Font styles to use
Other font styles liked:
• Something modern but dont mind that much

Colors
0054AA
0677BA
7BADD7
CADEEF
E8F1F8
00AB8E
00BBA5
67D7C9
C6EFE9
E9F9F6
EB3D1F
EC4F4E
F09395
F8D3D4
FCEDEE

Requirements
Must have
• a combined logo- new one

```html
<!DOCTYPE html>
<html lang="en">
<head>
<meta charset="utf-8">
<title>2024 Christmas Label – Fenwick &amp; Dorr, KRTL &amp; Brightwave</title>
<link rel="stylesheet" href="https://fonts.googleapis.com/css2?family=Playfair+Display:wght@900&family=Montserrat:wght@400;600&display=swap">
<style>
  :root {
    --frost: #cfe4e9;
    --frost-deep: #b4d3dc;
    --frost-ring: #a9cbd6;
    --pine: #3b6b46;
    --ink: #121a17;
    --ink-soft: #2a2f2d;
  }
  * { margin: 0; padding: 0; box-sizing: border-box; }
  html, body { width: 1200px; height: 1200px; overflow: hidden; }
  body { background: var(--frost); }

  .label {
    position: relative;
    width: 1200px;
    height: 1200px;
    background: radial-gradient(circle at 50% 45%, #d6e9ed 0%, var(--frost) 70%);
    overflow: hidden;
  }

  .label__halo {
    position: absolute;
    left: 243px; top: 235px;
    width: 710px; height: 710px;
    border-radius: 50%;
    background: var(--frost-deep);
    box-shadow: 0 0 0 8px rgba(169, 203, 214, 0.45), 0 0 0 18px rgba(169, 203, 214, 0.2);
  }

  .year {
    position: absolute;
    left: 0; right: 0;
    top: 318px;
    text-align: center;
    font-family: "Playfair Display", serif;
    font-weight: 900;
    font-size: 400px;
    line-height: 1;
    letter-spacing: -28px;
    color: var(--ink);
  }
  .year__digit--pine { color: var(--pine); }

  .rule {
    position: absolute;
    left: 82px; top: 682px;
    width: 1036px; height: 2px;
    background: var(--ink);
  }

  .partners {
    position: absolute;
    top: 716px; left: 0; right: 0;
    height: 98px;
  }
  .partner-name {
    position: absolute;
    font-family: "Montserrat", sans-serif;
    font-weight: 400;
    color: var(--ink-soft);
  }
  .partner-name--left {
    left: 298px; top: 12px;
    font-size: 34px;
    line-height: 1.05;
  }
  .partner-name--right {
    left: 728px; top: 24px;
    font-size: 46px;
    letter-spacing: 1px;
  }
  .divider {
    position: absolute;
    top: 2px;
    width: 1.5px; height: 96px;
    background: var(--ink-soft);
  }
  .divider--left { left: 517px; }
  .divider--right { left: 682px; }
  .snowflake {
    position: absolute;
    left: 564px; top: 20px;
  }

  .greeting {
    position: absolute;
    left: 0; right: 0;
    top: 886px;
    text-align: center;
    font-family: "Montserrat", sans-serif;
    font-weight: 600;
    font-size: 19px;
    line-height: 36px;
    color: var(--ink-soft);
  }
</style>
</head>
<body>
  <main class="label">
    <div class="label__halo"></div>

    <h1 class="year" aria-label="2024">
      <span class="year__digit">2</span><span class="year__digit year__digit--pine">0</span><span class="year__digit">2</span><span class="year__digit year__digit--pine">4</span>
    </h1>

    <div class="rule"></div>

    <section class="partners">
      <div class="partner-name partner-name--left">Fenwick<br>&amp; Dorr</div>
      <div class="divider divider--left"></div>
      <svg class="snowflake" width="72" height="60" viewBox="0 0 72 60" aria-label="Snowflake">
        <g stroke="#2a2f2d" stroke-width="1.6" fill="none" stroke-linecap="round">
          <line x1="36" y1="4" x2="36" y2="56"/>
          <line x1="13" y1="17" x2="59" y2="43"/>
          <line x1="13" y1="43" x2="59" y2="17"/>
          <polyline points="30,8 36,14 42,8"/>
          <polyline points="30,52 36,46 42,52"/>
          <polyline points="14,24 22,22 19,14"/>
          <polyline points="58,36 50,38 53,46"/>
          <polyline points="14,36 22,38 19,46"/>
          <polyline points="58,24 50,22 53,14"/>
        </g>
      </svg>
      <div class="divider divider--right"></div>
      <div class="partner-name partner-name--right">KRTL</div>
    </section>

    <p class="greeting">2024 Merry Christmas from the<br>Fenwick &amp; Dorr, KRTL &amp; Brightwave</p>
  </main>
</body>
</html>
```